Talvick Industrial Maintenance Business Card

Design a business card with the following information, logo must be included.
Talvick Industrial Maintenance
Dan Pelfrey Jr.
Pone 555-214-7608
email dan.pelfrey.jr@mailvantor.com

```html
<!DOCTYPE html>
<html lang="en">
<head>
<meta charset="utf-8">
<title>Talvick Industrial Maintenance – Business Card</title>
<link rel="stylesheet" href="https://fonts.googleapis.com/css2?family=Montserrat:wght@400;500;600;700&display=swap">
<style>
  :root {
    --backdrop: #d9d6d0;
    --card: #2a2a2c;
    --card-edge: #1d1d1f;
    --emboss-dark: #1f1f21;
    --emboss-light: #4a4a4d;
    --brand-blue: #1a72c2;
    --text-light: #e6e6e6;
    --text-muted: #8c8c8f;
  }
  * { box-sizing: border-box; margin: 0; padding: 0; }
  html, body {
    width: 900px; height: 1200px; overflow: hidden;
    background: var(--backdrop);
    font-family: "Montserrat", sans-serif;
  }
  .canvas { position: relative; width: 900px; height: 1200px; }
  .card {
    position: absolute; left: 80px; width: 742px; height: 440px;
    background: var(--card);
    border-radius: 30px;
    overflow: hidden;
    box-shadow: 0 6px 14px rgba(0,0,0,.35);
  }
  .card--front { top: 132px; }
  .card--back { top: 640px; height: 438px; }

  /* Front */
  .front-mark {
    position: absolute; left: 92px; top: 140px;
    display: flex; align-items: center; gap: 26px;
  }
  .front-mark__dot {
    width: 150px; height: 150px; border-radius: 50%;
    background: var(--emboss-dark);
    flex: none;
  }
  .front-mark__name {
    font-weight: 700; font-size: 40px; line-height: 1.1;
    color: var(--emboss-light);
    text-transform: uppercase;
    width: 420px;
  }

  /* Back */
  .company-name {
    position: absolute; left: 38px; top: 40px;
    font-weight: 700; font-size: 34px; line-height: 1.1;
    color: var(--brand-blue);
    text-transform: uppercase;
    width: 380px;
  }
  .back-decor {
    position: absolute; left: 440px; top: 10px;
    width: 340px; height: 340px; border-radius: 50%;
    background: linear-gradient(135deg, #1e1e20 0%, #2f2f31 60%, #3c3c3f 100%);
  }
  .contact { position: absolute; left: 38px; top: 282px; }
  .contact__name {
    font-weight: 600; font-size: 22px; color: var(--brand-blue);
  }
  .contact__title {
    font-size: 15px; color: var(--text-light); margin-top: 2px;
  }
  .contact__rule {
    width: 18px; height: 2px; background: var(--brand-blue);
    margin: 10px 0 14px 2px;
  }
  .contact__line {
    display: flex; align-items: center; gap: 9px;
    font-size: 15px; color: var(--text-light); margin-bottom: 6px;
  }
  .contact__icon { width: 18px; height: 18px; flex: none; }
</style>
</head>
<body>
<div class="canvas">

  <section class="card card--front">
    <div class="front-mark">
      <div class="front-mark__dot"></div>
      <div class="front-mark__name">Talvick Industrial Maintenance</div>
    </div>
  </section>

  <section class="card card--back">
    <div class="back-decor"></div>
    <div class="company-name">Talvick Industrial Maintenance</div>

    <div class="contact">
      <div class="contact__name">Dan Pelfrey Jr.</div>
      <div class="contact__title">CEO &amp; Founder</div>
      <div class="contact__rule"></div>
      <div class="contact__line">
        <svg class="contact__icon" viewBox="0 0 18 18" aria-hidden="true">
          <circle cx="9" cy="9" r="9" fill="var(--brand-blue)"/>
          <path d="M6 4.5l1.6 0 .8 2.2-1 .8a6 6 0 0 0 2.9 2.9l.8-1 2.2.8v1.6c0 .6-.5 1-1 1A8 8 0 0 1 5 5.5c0-.5.4-1 1-1z" fill="var(--card)"/>
        </svg>
        555-214-7608
      </div>
      <div class="contact__line">
        <svg class="contact__icon" viewBox="0 0 18 18" aria-hidden="true">
          <circle cx="9" cy="9" r="9" fill="var(--brand-blue)"/>
          <rect x="4.5" y="5.8" width="9" height="6.4" rx="1" fill="var(--card)"/>
          <path d="M4.8 6.2L9 9.3l4.2-3.1" stroke="var(--brand-blue)" stroke-width="1" fill="none"/>
        </svg>
        dan.pelfrey.jr@mailvantor.com
      </div>
    </div>
  </section>

</div>
</body>
</html>
```